Quorvex - Automated robotic Inspection with AI need new business cards

We need a new design of our business cards. The company is focused on automated quality control at high speed with unmatched results. We have a logo but need a more forward leaning business card that shows that we are delivering cutting edge technology.

Contact Information for Business Card

Name
Position
Adress
Phone
Email
e.g.
Lena Holmqvist
Chief Financial Officer (CFO)

Quorvex Sweden AB
Bruksvägen 14, SE-175 43 JÄRFÄLLA, Sweden
Mobile: +46735 21 47 83 | Office: +46 8 61 94 27
www.quorvex-example.com

Font styles to use
Sans Serif

```html
<!DOCTYPE html>
<html lang="en">
<head>
<meta charset="utf-8">
<title>Quorvex business card</title>
<link rel="stylesheet" href="https://fonts.googleapis.com/css2?family=Roboto:wght@400;500;700&display=swap">
<style>
  :root {
    --brand-blue: #1b5a8a;
    --ink-dark: #333333;
    --ink-soft: #666666;
    --card-white: #ffffff;
    --backdrop: #ececec;
  }
  html, body {
    margin: 0;
    padding: 0;
    overflow: hidden;
  }
  body {
    width: 1125px;
    height: 1200px;
    background: var(--backdrop);
    position: relative;
    font-family: "Roboto", sans-serif;
  }
  .card {
    position: absolute;
    left: 171px;
    width: 826px;
    border-radius: 24px;
    overflow: hidden;
  }
  .card-front {
    top: 106px;
    height: 472px;
    background: var(--brand-blue);
  }
  .card-front .face {
    position: absolute;
    inset: 0 0 15px 0;
    background: var(--card-white);
    border-radius: 24px;
  }
  .front-wordmark {
    position: absolute;
    left: 285px;
    top: 182px;
    transform: translateX(-50%);
    margin: 0;
    font-size: 52px;
    font-weight: 500;
    letter-spacing: 1px;
    color: var(--brand-blue);
    text-transform: uppercase;
  }
  .divider {
    position: absolute;
    left: 445px;
    top: 116px;
    width: 2px;
    height: 242px;
    background: var(--brand-blue);
  }
  .contact-block {
    position: absolute;
    left: 480px;
    top: 108px;
  }
  .person-name {
    margin: 0;
    font-size: 25px;
    font-weight: 700;
    color: var(--brand-blue);
    text-transform: uppercase;
    line-height: 1.2;
  }
  .person-title {
    margin: 2px 0 0;
    font-size: 19px;
    color: var(--ink-dark);
  }
  .company-address {
    margin: 18px 0 0;
    font-style: normal;
    font-size: 18px;
    line-height: 23px;
    color: var(--ink-soft);
  }
  .contact-list {
    list-style: none;
    margin: 14px 0 0;
    padding: 0;
    font-size: 18px;
    line-height: 25px;
    color: var(--ink-soft);
  }
  .contact-list li {
    display: flex;
    align-items: center;
    gap: 10px;
  }
  .contact-list svg {
    width: 15px;
    height: 15px;
    fill: var(--brand-blue);
    flex: none;
  }
  .card-back {
    top: 640px;
    height: 469px;
    background: var(--brand-blue);
  }
  .back-wordmark {
    position: absolute;
    right: 50px;
    top: 300px;
    margin: 0;
    font-size: 70px;
    font-weight: 500;
    letter-spacing: 1px;
    color: var(--card-white);
    text-transform: uppercase;
    line-height: 1;
  }
  .back-web {
    position: absolute;
    right: 50px;
    top: 412px;
    margin: 0;
    font-size: 17px;
    font-weight: 700;
    letter-spacing: 3px;
    color: var(--card-white);
  }
</style>
</head>
<body>
  <section class="card card-front">
    <div class="face">
      <h1 class="front-wordmark">Quorvex</h1>
      <div class="divider"></div>
      <div class="contact-block">
        <h2 class="person-name">Lena Holmqvist</h2>
        <p class="person-title">Chief Financial Officer</p>
        <address class="company-address">
          Quorvex Sweden AB<br>
          Bruksvägen 14, SE-175 43<br>
          JÄRFÄLLA, Sweden
        </address>
        <ul class="contact-list">
          <li>
            <svg viewBox="0 0 16 16" aria-hidden="true"><path d="M3.5 1l2.5 3-1.5 1.8c.9 2 2.7 3.8 4.7 4.7L11 9l3 2.5-1.5 3C7 14.5 1.5 9 1.5 3.5z"/></svg>
            <span>+46 8 61 94 27</span>
          </li>
          <li>
            <svg viewBox="0 0 16 16" aria-hidden="true"><path d="M4 1h8v14H4zM5.5 3v9h5V3z"/></svg>
            <span>+46735 21 47 83</span>
          </li>
          <li>
            <svg viewBox="0 0 16 16" aria-hidden="true"><path d="M1 4h14v9H1zM2 5l6 4 6-4z"/></svg>
            <span>info@quorvex-example.com</span>
          </li>
          <li>
            <svg viewBox="0 0 16 16" aria-hidden="true"><circle cx="8" cy="8" r="7"/><path d="M5 4c2 1 1 3 3 3s1 3 3 3" stroke="#fff" stroke-width="1.4" fill="none"/></svg>
            <span>www.quorvex-example.com</span>
          </li>
        </ul>
      </div>
    </div>
  </section>

  <section class="card card-back">
    <h2 class="back-wordmark">Quorvex</h2>
    <p class="back-web">www.quorvex-example.com</p>
  </section>
</body>
</html>
```